Präsentationsvorlagen/Workbook für Coaching - Yoga - Training
Zielgruppe
Coaching - Yoga - Training, d.h. Yogaunterricht, Einzelcoaching, Seminare und Workshops rund um das Thema Stress/Resilienz/Achtsamkeit
Zielgruppe sind einerseits überwiegend Frauen, aber auch Firmenkunden, die für ihre Mitarbeiter Seminare und Yoga anbieten.
Aufgabenstellung
Ich benötige einen professionellen ppt Auftritt für Präsentationen/Workbooks mit meinen Firmenfarben (grau, weiß, rosa, beige) in den mein Logo integriert ist.
Das Design sollte dem Thema entsprechend 'warm' sein aber die nötige Professionalität für Firmenkunden ausstrahlen.

```html
<!DOCTYPE html>
<html lang="de">
<head>
<meta charset="utf-8">
<title>Präsentationsvorlagen – Yoga &amp; Coaching</title>
<link href="https://fonts.googleapis.com/css2?family=Cinzel:wght@400&family=Lato:wght@400&display=swap" rel="stylesheet">
<style>
:root{
  --beige:#c8b39c;
  --beige-light:#dccbb9;
  --band:rgba(214,193,172,.82);
  --frame:#d6c6b2;
  --rose:#e4a3a3;
  --grey:#6e6e6e;
  --grey-dark:#4a4a4a;
  --photo-wall:#e4e2df;
  --photo-floor:#c8b3a0;
  --white:#ffffff;
}
*{margin:0;padding:0;box-sizing:border-box}
html,body{width:848px;height:1200px;overflow:hidden;background:var(--white)}
.sheet{position:relative;width:848px;height:1200px}
.slide{position:absolute;width:368px;height:207px;border:1px solid var(--frame);background:var(--white);overflow:hidden}
.col-left{left:36px}.col-right{left:438px}
.row-1{top:74px}.row-2{top:293px}.row-3{top:511px}.row-4{top:729px}
.photo{position:absolute;background:linear-gradient(180deg,var(--photo-wall) 0%,#ecebe8 62%,var(--photo-floor) 78%,#b9a08e 100%)}
.photo-full{inset:0}
.photo-side{left:183px;top:0;width:185px;height:207px;background:linear-gradient(180deg,#e2e0dd 0%,#d6d3cf 70%,#a9937f 88%,#8fb3d2 100%)}
.slide-title{position:absolute;font-family:"Cinzel",serif;font-variant:small-caps;color:var(--grey-dark);font-size:15px;letter-spacing:.5px;white-space:nowrap}
.band{position:absolute;left:0;right:0;top:133px;height:36px;background:var(--band)}
.band .slide-title{position:static;display:block;text-align:center;line-height:36px;color:var(--white);font-size:16px}
.body-text{position:absolute;font-family:"Lato",sans-serif;font-size:5.3px;line-height:8.6px;color:var(--rose)}
.body-text u{text-decoration-color:var(--rose)}
.body-text p+p{margin-top:6px}
.icon-row{position:absolute;display:flex;align-items:center;gap:12px}
.icon-row .body-text{position:static}
.brand{position:absolute;left:8px;bottom:6px;display:flex;flex-direction:column;align-items:center;gap:1px}
.brand-dot{width:6px;height:6px;border-radius:50%;background:var(--rose)}
.brand-name{font-family:"Cinzel",serif;font-size:3.6px;color:var(--grey);letter-spacing:.3px}
.yoga-box{position:absolute;left:35px;top:56px;width:72px;height:120px;background:var(--beige);padding:7px 7px}
.yoga-box h3{font-family:"Cinzel",serif;font-weight:400;color:var(--white);font-size:10px;margin-bottom:8px}
.yoga-box .body-text{position:static;color:var(--white)}
.chart{position:absolute;font-family:"Lato",sans-serif}
</style>
</head>
<body>
<main class="sheet">

  <section class="slide col-left row-1">
    <div class="photo photo-full" role="img" aria-label="Foto: Frau in der Yoga-Haltung herabschauender Hund auf einer Matte"></div>
    <div class="band"><h1 class="slide-title">Titelfolie V1</h1></div>
  </section>

  <section class="slide col-right row-1">
    <div class="photo photo-full" role="img" aria-label="Foto: Frau in der Yoga-Haltung herabschauender Hund auf einer Matte"></div>
    <h1 class="slide-title" style="left:29px;top:42px;font-size:16px">Titelfolie V2</h1>
  </section>

  <section class="slide col-left row-2">
    <h1 class="slide-title" style="left:42px;top:92px;font-size:15px">Titelfolie V3</h1>
    <div class="photo photo-side" role="img" aria-label="Foto: Frau in einer Rückbeuge auf einer Yogamatte vor einer Marmorwand"></div>
  </section>

  <section class="slide col-right row-2">
    <h2 class="slide-title" style="left:22px;top:20px;font-size:14px">Textseite mit Icons</h2>
    <div class="icon-row" style="left:28px;top:72px">
      <svg width="34" height="34" viewBox="0 0 34 34" aria-hidden="true"><circle cx="17" cy="17" r="17" fill="var(--beige-light)"/><path d="M10 21 Q17 25 24 21 M17 20 V13 M17 15 Q13 12 12 9 Q16 10 17 15 Q18 10 22 9 Q21 12 17 15" stroke="#fff" stroke-width="1.2" fill="none"/></svg>
      <div class="body-text"><u>Lorem ipsum dolor sit amet</u></div>
    </div>
    <div class="icon-row" style="left:28px;top:116px">
      <svg width="34" height="34" viewBox="0 0 34 34" aria-hidden="true"><circle cx="17" cy="17" r="17" fill="var(--beige-light)"/><path d="M17 9 Q21 14 17 22 Q13 14 17 9 Z M17 22 Q11 20 9 14 Q14 15 17 22 Q20 15 25 14 Q23 20 17 22 Z" stroke="#fff" stroke-width="1.1" fill="none"/></svg>
      <div class="body-text"><u>Lorem ipsum dolor sit amet</u></div>
    </div>
    <div class="icon-row" style="left:204px;top:78px">
      <svg width="26" height="20" viewBox="0 0 26 20" aria-hidden="true"><path d="M13 4 Q7 1 2 2 V17 Q7 16 13 19 Q19 16 24 17 V2 Q19 1 13 4 Z M13 4 V19" stroke="var(--beige)" stroke-width="1.1" fill="none"/></svg>
      <div class="body-text"><u>Lorem ipsum dolor sit amet</u></div>
    </div>
    <div class="icon-row" style="left:204px;top:124px">
      <svg width="26" height="20" viewBox="0 0 26 20" aria-hidden="true"><path d="M13 3 Q17 9 13 16 Q9 9 13 3 Z M13 16 Q7 14 5 8 Q10 9 13 16 Q16 9 21 8 Q19 14 13 16 Z M13 16 Q5 17 1 12 M13 16 Q21 17 25 12" stroke="var(--beige)" stroke-width="1" fill="none"/></svg>
      <div class="body-text"><u>Lorem ipsum dolor sit amet</u></div>
    </div>
    <div class="brand"><span class="brand-dot"></span><span class="brand-name">Lena Hartmann</span></div>
  </section>

  <section class="slide col-left row-3">
    <h2 class="slide-title" style="left:22px;top:18px;font-size:14px">Textseite V1</h2>
    <div class="body-text" style="left:35px;top:60px;width:236px">
      <p><u>Lorem ipsum dolor sit amet, consetetur sadipscing elitr</u>, sed <u>diam nonumy eirmod tempor invidunt ut labore</u> et <u>dolore</u> magna <u>aliquyam erat</u>, sed <u>diam voluptua. Lorem ipsum dolor sit amet, consetetur sadipscing elitr</u>, sed <u>diam nonumy eirmod tempor invidunt ut labore</u> et <u>dolore</u> magna <u>aliquyam erat</u>, sed <u>diam voluptua</u>.</p>
      <p><u>Lorem ipsum dolor sit amet, consetetur sadipscing elitr</u>, sed <u>diam nonumy eirmod tempor invidunt ut labore</u> et <u>dolore</u> magna <u>aliquyam erat</u>, sed <u>diam voluptua</u>. <u>Lorem ipsum dolor sit amet, consetetur sadipscing elitr</u>, sed <u>diam nonumy eirmod tempor invidunt ut labore</u> et <u>dolore</u> magna <u>aliquyam erat</u>, sed <u>diam voluptua</u>.</p>
    </div>
    <div class="brand"><span class="brand-dot"></span><span class="brand-name">Lena Hartmann</span></div>
  </section>

  <section class="slide col-right row-3">
    <h2 class="slide-title" style="left:22px;top:18px;font-size:14px">Textseite V2</h2>
    <div class="yoga-box">
      <h3>Yoga</h3>
      <div class="body-text"><u>Lorem ipsum dolor sit amet, consetetur sadipscing elitr, sed diam nonumy</u></div>
    </div>
    <div class="body-text" style="left:135px;top:84px;width:152px">
      <p><u>Lorem ipsum dolor sit amet, consetetur sadipscing elitr</u>, sed <u>diam nonumy eirmod tempor invidunt ut labore</u> et <u>dolore</u> magna <u>aliquyam erat</u>, sed <u>diam voluptua</u>. <u>Lorem ipsum dolor sit amet, consetetur sadipscing elitr</u>, sed <u>diam nonumy eirmod tempor invidunt ut labore</u> et <u>dolore</u> magna <u>aliquyam erat</u>, sed <u>diam voluptua</u>.</p>
    </div>
    <div class="brand"><span class="brand-dot"></span><span class="brand-name">Lena Hartmann</span></div>
  </section>

  <section class="slide col-left row-4">
    <h2 class="slide-title" style="left:22px;top:18px;font-size:14px">Diagramme</h2>
    <svg class="chart" style="left:25px;top:62px" width="170" height="92" viewBox="0 0 170 92" font-size="4.5" fill="var(--grey)">
      <text x="90" y="6" text-anchor="middle" font-size="5.5">Diagrammtitel</text>
      <g stroke="#e6e6e6" stroke-width=".5">
        <line x1="12" y1="16" x2="165" y2="16"/><line x1="12" y1="26.6" x2="165" y2="26.6"/><line x1="12" y1="37.2" x2="165" y2="37.2"/><line x1="12" y1="47.8" x2="165" y2="47.8"/><line x1="12" y1="58.4" x2="165" y2="58.4"/><line x1="12" y1="69" x2="165" y2="69"/>
      </g>
      <g text-anchor="end"><text x="8" y="18">5</text><text x="8" y="28.5">4</text><text x="8" y="39">3</text><text x="8" y="49.6">2</text><text x="8" y="60.2">1</text><text x="8" y="70.8">0</text></g>
      <g fill="var(--beige)"><rect x="20" y="23" width="7" height="46"/><rect x="58" y="43" width="7" height="26"/><rect x="96" y="32" width="7" height="37"/><rect x="134" y="21" width="7" height="48"/></g>
      <g fill="var(--grey)"><rect x="29" y="44" width="7" height="25"/><rect x="67" y="21" width="7" height="48"/><rect x="105" y="50" width="7" height="19"/><rect x="143" y="39" width="7" height="30"/></g>
      <g text-anchor="middle"><text x="28" y="77">Kategorie 1</text><text x="66" y="77">Kategorie 2</text><text x="104" y="77">Kategorie 3</text><text x="142" y="77">Kategorie 4</text></g>
      <rect x="52" y="83" width="3" height="3" fill="var(--beige)"/><text x="57" y="86">Datenreihe 1</text>
      <rect x="88" y="83" width="3" height="3"/><text x="93" y="86">Datenreihe 2</text>
    </svg>
    <svg class="chart" style="left:195px;top:62px" width="165" height="92" viewBox="0 0 165 92" font-size="4.5" fill="var(--grey)">
      <text x="85" y="6" text-anchor="middle" font-size="5.5">Diagrammtitel</text>
      <g stroke="#e6e6e6" stroke-width=".5">
        <line x1="10" y1="16" x2="160" y2="16"/><line x1="10" y1="26.6" x2="160" y2="26.6"/><line x1="10" y1="37.2" x2="160" y2="37.2"/><line x1="10" y1="47.8" x2="160" y2="47.8"/><line x1="10" y1="58.4" x2="160" y2="58.4"/><line x1="10" y1="69" x2="160" y2="69"/>
      </g>
      <g text-anchor="end"><text x="7" y="18">5</text><text x="7" y="28.5">4</text><text x="7" y="39">3</text><text x="7" y="49.6">2</text><text x="7" y="60.2">1</text><text x="7" y="70.8">0</text></g>
      <polyline points="28,23 66,43 104,37 142,21" fill="none" stroke="var(--grey)" stroke-width="1"/>
      <polyline points="28,44 66,21 104,50 142,39" fill="none" stroke="var(--beige)" stroke-width="1"/>
      <g text-anchor="middle"><text x="28" y="77">Kategorie 1</text><text x="66" y="77">Kategorie 2</text><text x="104" y="77">Kategorie 3</text><text x="142" y="77">Kategorie 4</text></g>
      <line x1="40" y1="84.5" x2="46" y2="84.5" stroke="var(--grey)"/><text x="48" y="86">Datenreihe 1</text>
      <line x1="80" y1="84.5" x2="86" y2="84.5" stroke="var(--beige)"/><text x="88" y="86">Datenreihe 2</text>
    </svg>
    <div class="brand"><span class="brand-dot"></span><span class="brand-name">Lena Hartmann</span></div>
  </section>

  <section class="slide col-right row-4">
    <h2 class="slide-title" style="left:20px;top:18px;font-size:14px">Diagramme</h2>
    <svg class="chart" style="left:18px;top:62px" width="175" height="92" viewBox="0 0 175 92" font-size="4.5" fill="var(--grey)">
      <text x="92" y="8" text-anchor="middle" font-size="5.5">Diagrammtitel</text>
      <g stroke="#e6e6e6" stroke-width=".5">
        <line x1="34" y1="14" x2="34" y2="70"/><line x1="61" y1="14" x2="61" y2="70"/><line x1="88" y1="14" x2="88" y2="70"/><line x1="115" y1="14" x2="115" y2="70"/><line x1="142" y1="14" x2="142" y2="70"/><line x1="169" y1="14" x2="169" y2="70"/>
      </g>
      <rect x="34" y="21" width="120" height="7" fill="var(--beige)"/>
      <rect x="34" y="29" width="69" height="7" fill="var(--grey)"/>
      <rect x="34" y="48" width="66" height="7" fill="var(--beige)"/>
      <rect x="34" y="56" width="118" height="7" fill="var(--grey)"/>
      <g text-anchor="end"><text x="30" y="30">Kategorie 2</text><text x="30" y="57">Kategorie 1</text></g>
      <g text-anchor="middle"><text x="34" y="77">0</text><text x="61" y="77">1</text><text x="88" y="77">2</text><text x="115" y="77">3</text><text x="142" y="77">4</text><text x="169" y="77">5</text></g>
      <rect x="60" y="84" width="3" height="3" fill="var(--rose)"/><text x="65" y="87">Datenreihe 1</text>
      <rect x="98" y="84" width="3" height="3"/><text x="103" y="87">Datenreihe 2</text>
    </svg>
    <svg class="chart" style="left:235px;top:62px" width="80" height="92" viewBox="0 0 80 92" font-size="4.5" fill="var(--grey)">
      <text x="40" y="8" text-anchor="middle" font-size="5.5">Verkauf</text>
      <path d="M40 46 L40 16 A30 30 0 1 1 10.5 41 Z" fill="var(--grey)"/>
      <path d="M40 46 L10.5 41 A30 30 0 0 1 40 16 Z" fill="var(--beige)"/>
      <rect x="12" y="84" width="3" height="3"/><text x="17" y="87">1. Quartal</text>
      <rect x="42" y="84" width="3" height="3" fill="var(--beige)"/><text x="47" y="87">2. Quartal</text>
    </svg>
    <div class="brand"><span class="brand-dot"></span><span class="brand-name">Lena Hartmann</span></div>
  </section>

</main>
</body>
</html>
```